7' x 4' sign for a new multiunit residential mountain location**

Our mission is to build people their dream home through the use of professional and thoughtful design. We're a new developer, building a new and feature-filled fourplex, and need a brand and presence that generates interests and builds our brand. Our homes are professionally and thoughtfully designed - we agonize over the details so our homeowners don't have to once they move in.

We're constructing a new fourplex in downtown Cedarvale, BC, Canada. The location is in the heart of the city's entertainment and cultural zones, is surrounded by mountains and a lake, and within an hour of over 100 wineries. "Valley" residents prize their time outdoors - boating, biking, hiking, skiing, and more. It's no wonder Cedarvale is often cited as one of the most beautiful and desirable places to live in the world.

attachments - brand elements, rendering of the unit, feature sheet for each unit, and picture of the sign casing (7' wide and 4' long envelop - pic of sign frame attached).

Target Market(s)

Young professionals (age 30 to 45); Empty nestes (age 55+)

Font styles to use
Other font styles liked:
• Cordia New

Requirements
Must have
• Our tag line - CRAFTED TO LIVE

Presence - this is an unusual shape and large sign. It must create interest and build our brand.

```html
<!DOCTYPE html>
<html lang="en">
<head>
<meta charset="utf-8">
<title>612 Dalton — Crafted to Live</title>
<link rel="stylesheet" href="https://fonts.googleapis.com/css2?family=Marcellus&family=Tinos&display=swap">
<style>
  :root {
    --sign-plum: #332a35;
    --sign-silver: #aca8ad;
    --peak-light: #b9b5ba;
    --peak-dark: #6d6770;
  }
  * { margin: 0; padding: 0; box-sizing: border-box; }
  html, body {
    width: 1200px;
    height: 667px;
    overflow: hidden;
    background: var(--sign-plum);
  }
  .sign {
    position: relative;
    width: 1200px;
    height: 667px;
    background: var(--sign-plum);
    color: var(--sign-silver);
  }
  .sign__address,
  .sign__tagline,
  .sign__location {
    position: absolute;
    left: 0;
    right: 0;
    text-align: center;
    line-height: 1;
    white-space: nowrap;
    font-weight: 400;
  }
  .sign__address {
    top: 75px;
    font-family: "Marcellus", serif;
    font-size: 150px;
    letter-spacing: 16px;
    padding-left: 16px;
  }
  .sign__horizon {
    position: absolute;
    left: 0;
    top: 0;
    width: 1200px;
    height: 667px;
  }
  .horizon-line { stroke: var(--sign-silver); stroke-width: 3; }
  .peak-top { stop-color: var(--peak-light); stop-opacity: 0.85; }
  .peak-base { stop-color: var(--peak-dark); stop-opacity: 0.5; }
  .sign__tagline {
    top: 346px;
    font-family: "Tinos", serif;
    font-size: 86px;
    letter-spacing: 3px;
  }
  .sign__location {
    top: 443px;
    font-family: "Tinos", serif;
    font-size: 66px;
  }
</style>
</head>
<body>
  <main class="sign">
    <h1 class="sign__address">612 DALTON</h1>

    <svg class="sign__horizon" viewBox="0 0 1200 667">
      <defs>
        <linearGradient id="peak-tone" x1="0" y1="0" x2="0" y2="1">
          <stop class="peak-top" offset="0"/>
          <stop class="peak-base" offset="1"/>
        </linearGradient>
      </defs>
      <line class="horizon-line" x1="88" y1="275" x2="448" y2="275"/>
      <rect class="mountain-art" x="448" y="219" width="349" height="58" fill="url(#peak-tone)" role="img" aria-label="Silhouette of a mountain range rising from the horizon line"/>
      <line class="horizon-line" x1="797" y1="277" x2="1114" y2="277"/>
    </svg>

    <p class="sign__tagline">CRAFTED TO LIVE</p>
    <p class="sign__location">Cedarvale, BC, Canada</p>
  </main>
</body>
</html>
```